RICE AND RUN WALL POSTER

Hi designer,

I would like to create a poster to put on my wall.

My intention is to place a bicycle onto a wall and have these words vinyl stick next to it.

" Life is not a race.
It is a journey
Enjoy each moment. Relax!
Have a bowl of Rice and Run
Make all your dreams come true "

I like traditional fonts - easy to read. See example. This is something I would love.

It will be on a white wall so black text would be ok. I have also attached my logo - maybe try include Rice and Run font in your design if possible - but not important.

Good luck everyone.

Font styles to use
Decorative
Script

Requirements
Must have
• The placement of my bike will be on the top left corner of the wall so I think it will be best fit if all designs are done in horizontal rectangular shape (landscape)

```html
<!DOCTYPE html>
<html lang="en">
<head>
<meta charset="UTF-8">
<title>Rice and Run Wall Poster</title>
<link rel="stylesheet" href="https://fonts.googleapis.com/css2?family=Archivo+Black&family=Kaushan+Script&family=Bebas+Neue&family=Arvo:wght@700&family=Ultra&family=Syncopate:wght@700&display=swap">
<style>
  :root {
    --paper: #ffffff;
    --ink: #111111;
  }
  html, body {
    margin: 0;
    padding: 0;
    width: 1200px;
    height: 1123px;
    overflow: hidden;
    background: var(--paper);
  }
  .poster {
    position: relative;
    width: 1200px;
    height: 1123px;
    background: var(--paper);
    color: var(--ink);
  }
  .line {
    position: absolute;
    margin: 0;
    white-space: nowrap;
    line-height: 1;
    transform-origin: left center;
  }
  .script {
    font-family: "Kaushan Script", cursive;
    font-weight: 400;
  }
  .life {
    left: 100px;
    top: 280px;
    font-family: "Archivo Black", sans-serif;
    font-size: 118px;
    transform: rotate(-13deg);
  }
  .not-race {
    left: 226px;
    top: 400px;
    font-size: 46px;
    transform: rotate(8deg);
  }
  .enjoy {
    left: 48px;
    top: 494px;
    font-size: 50px;
    transform: rotate(-3deg);
  }
  .bowl {
    left: 148px;
    top: 640px;
    font-size: 50px;
    transform: rotate(-13deg);
  }
  .dreams {
    left: 70px;
    top: 808px;
    font-size: 46px;
    transform: rotate(-21deg);
  }
  .come-true {
    left: 372px;
    top: 836px;
    font-size: 104px;
    transform: rotate(-20deg);
  }
  .it-is-a {
    left: 553px;
    top: 298px;
    font-family: "Bebas Neue", sans-serif;
    font-size: 50px;
  }
  .journey {
    position: absolute;
    left: 530px;
    top: 350px;
    width: 510px;
    height: 110px;
  }
  .journey text {
    font-family: "Arvo", serif;
    font-weight: 700;
    font-size: 60px;
    fill: var(--ink);
  }
  .relax {
    left: 548px;
    top: 470px;
    font-family: "Ultra", serif;
    font-size: 86px;
    letter-spacing: 2px;
  }
  .brand-name {
    position: absolute;
    left: 537px;
    top: 568px;
    width: 625px;
    height: 84px;
  }
  .brand-name text {
    font-family: "Syncopate", sans-serif;
    font-weight: 700;
    font-size: 74px;
    fill: var(--ink);
  }
</style>
</head>
<body>
  <main class="poster">
    <p class="line life">LIFE</p>
    <p class="line script not-race">is not a race.</p>
    <p class="line script enjoy">Enjoy each moment.</p>
    <p class="line script bowl">Have a bowl of</p>
    <p class="line script dreams">Make all your dreams</p>
    <p class="line script come-true">come true</p>

    <p class="line it-is-a">IT IS A</p>

    <svg class="journey" viewBox="0 0 510 110" aria-label="Journey">
      <defs>
        <path id="journey-arc" d="M 14 98 Q 255 20 496 98"/>
      </defs>
      <text>
        <textPath href="#journey-arc" startOffset="50%" text-anchor="middle" textLength="470" lengthAdjust="spacing">JOURNEY</textPath>
      </text>
    </svg>

    <p class="line relax">Relax!</p>

    <svg class="brand-name" viewBox="0 0 625 84" aria-label="Rice and Run">
      <text x="0" y="74" textLength="623" lengthAdjust="spacingAndGlyphs">RICE &amp; RUN</text>
    </svg>
  </main>
</body>
</html>
```